plumbers buisness card

A buisness card for a plumbing buisness
needs to have a water theme with navy blue, light blue and white
with an image of either a water drop, pipes, tools or something relating to plumbing and incorperating my buisness name as a logo

"Kesterly Plumbing" is the words that need to stand out with "& gasfitting" to be smaller
Updates

spelling error on brief, "maintenance"
and also could you include my email m_kesterly@mailnest.com.au

Industry/Entity Type

Plumbing

Contact Information for Business Card

Kesterly Plumbing & Gasfitting

marcus kesterly
0493612085

specialising in
-new homes
-maitenance
-renovations

license no.
-73804

```html
<!DOCTYPE html>
<html lang="en">
<head>
<meta charset="utf-8">
<title>Kesterly Plumbing &amp; Gasfitting – Business Card</title>
<link href="https://fonts.googleapis.com/css2?family=Arimo:wght@400;700&family=Open+Sans:wght@600&family=Tinos:ital,wght@1,700&display=swap" rel="stylesheet">
<style>
  :root {
    --page: #ffffff;
    --edge: #d9fbfb;
    --cream: #fdfde6;
    --teal: #2aa1a6;
    --brand: #2aa9d2;
    --navy: #16335e;
    --panel: #1f1f1f;
    --gold: #f4b123;
    --white: #ffffff;
    --ink: #111111;
    --drop-light: #c8eef7;
    --drop-deep: #36b6d4;
  }
  html, body {
    margin: 0;
    padding: 0;
    width: 670px;
    height: 1200px;
    overflow: hidden;
    background: var(--page);
  }
  .canvas {
    position: relative;
    width: 670px;
    height: 1200px;
  }
  .owner-name {
    position: absolute;
    top: 58px;
    left: 0;
    width: 100%;
    margin: 0;
    text-align: center;
    font-family: "Open Sans", sans-serif;
    font-weight: 600;
    font-size: 40px;
    line-height: 54px;
    color: var(--ink);
  }
  .card {
    position: absolute;
    left: 76px;
    top: 126px;
    width: 514px;
    height: 1064px;
    background: var(--edge);
  }
  .card-face {
    position: absolute;
    left: 16px;
    right: 16px;
    top: 0;
    bottom: 0;
    background: var(--cream);
  }
  .brand {
    position: absolute;
    left: 0;
    right: 0;
    top: 118px;
    text-align: center;
    font-family: "Arimo", sans-serif;
    font-weight: 700;
    color: var(--brand);
    text-transform: uppercase;
  }
  .brand-name { display: block; font-size: 92px; line-height: 110px; letter-spacing: 2px; }
  .brand-trade { display: block; font-size: 56px; line-height: 60px; letter-spacing: 4px; }
  .brand-amp { display: block; font-size: 40px; line-height: 48px; }
  .brand-extra { display: block; font-size: 50px; line-height: 58px; letter-spacing: 4px; }
  .email {
    position: absolute;
    left: 0;
    right: 24px;
    top: 640px;
    margin: 0;
    text-align: right;
    font-family: "Arimo", sans-serif;
    font-size: 22px;
    color: var(--navy);
  }
  .contact-box {
    position: absolute;
    left: 248px;
    top: 810px;
    width: 308px;
    height: 346px;
    background: var(--teal);
  }
  .phone {
    position: absolute;
    left: 20px;
    top: 14px;
    margin: 0;
    font-family: "Arimo", sans-serif;
    font-size: 31px;
    line-height: 40px;
    color: var(--white);
  }
  .services-panel {
    position: absolute;
    left: 0;
    top: 874px;
    width: 520px;
    height: 262px;
    background: var(--panel);
  }
  .tap-image {
    position: absolute;
    left: 0;
    top: 20px;
    width: 150px;
    height: 222px;
    border-radius: 0 40px 40px 0;
    background: linear-gradient(160deg, var(--drop-light), var(--drop-deep) 60%, var(--navy));
  }
  .services {
    position: absolute;
    left: 286px;
    top: 10px;
  }
  .services-lead {
    margin: 0;
    font-family: "Tinos", serif;
    font-style: italic;
    font-weight: 700;
    font-size: 31px;
    line-height: 40px;
    color: var(--white);
  }
  .service-list {
    list-style: none;
    margin: 4px 0 0;
    padding: 0;
    font-family: "Arimo", sans-serif;
    font-size: 32px;
    line-height: 48px;
    color: var(--gold);
  }
  .license {
    position: absolute;
    left: 286px;
    top: 226px;
    margin: 0;
    font-family: "Arimo", sans-serif;
    font-size: 24px;
    line-height: 28px;
    color: var(--white);
  }
</style>
</head>
<body>
<main class="canvas">
  <h1 class="owner-name">Marcus Kesterly</h1>

  <section class="card">
    <div class="card-face">
      <div class="brand">
        <span class="brand-name">Kesterly</span>
        <span class="brand-trade">Plumbing</span>
        <span class="brand-amp">&amp;</span>
        <span class="brand-extra">Gasfitting</span>
      </div>
      <p class="email">m_kesterly@mailnest.com.au</p>
    </div>
  </section>

  <div class="contact-box">
    <p class="phone">T: 0493612085</p>
  </div>

  <section class="services-panel">
    <div class="tap-image" role="img" aria-label="Illustration of a water tap with a falling water drop"></div>
    <div class="services">
      <p class="services-lead">Specialising in</p>
      <ul class="service-list">
        <li>New Homes</li>
        <li>Maintenance</li>
        <li>Renovations</li>
      </ul>
    </div>
    <p class="license">license no.73804</p>
  </section>
</main>
</body>
</html>
```